5 x Packaging Design - Most of the design style is already done!

The logo is "Fern And Flint" which will remain the same. The font is Athens.

We just require realistic packaging design with the fronts of the packaging. Together/ seperate/ in different mockup backdrops etc.

CLAY MASKS: BLACK JAR WHITE LID:
- the cursive coloured font is "Majesty"
- If you think you can design something even more attractive go for it! but we like the design a lot.
- Most important for us is to make it look realistic on the packaging so that we can use it on the website :)

BEARD OIL: BLACK JAR WITH SILVER AND WHITE PUMP LID:
- You are free to design similar/same or completely different

competitors:
Morvelle
reedandrain

Industry/Entity Type

Cosmetics

```html
<!DOCTYPE html>
<html lang="en">
<head>
<meta charset="utf-8">
<title>Fern And Flint — Jar Label Fronts</title>
<link rel="stylesheet" href="https://fonts.googleapis.com/css2?family=Josefin+Sans:wght@300;400&family=Caveat+Brush&family=Dancing+Script:wght@700&family=Oswald:wght@300&family=Lato:wght@400&display=swap">
<style>
  :root {
    --bg-top: #f1f1f0;
    --bg-bottom: #bdbcbc;
    --label: #1b1a2c;
    --label-edge: #2e2d44;
    --ink: #d9d9e2;
    --ink-soft: #a9a9ba;
    --lime: #b6e02a;
    --gold: #f3c21b;
    --pink: #ff5fd2;
    --crimson: #e0173e;
    --white: #f4f4f6;
    --arrow: #f7a531;
    --copy: #6f6f6f;
    --leaf: #7f977c;
  }
  * { margin: 0; padding: 0; box-sizing: border-box; }
  html, body { width: 1200px; height: 2399px; overflow: hidden; }
  body { font-family: "Josefin Sans", sans-serif; background: var(--bg-bottom); }
  .range { display: flex; flex-direction: column; width: 1200px; height: 2399px; }
  .product {
    position: relative;
    flex: 1;
    background: linear-gradient(to bottom, var(--bg-top), var(--bg-bottom));
    overflow: hidden;
  }
  .foliage {
    position: absolute; top: 135px; width: 260px; height: 250px;
    border-radius: 50%;
    background: radial-gradient(ellipse at center, rgba(127,151,124,.55), rgba(127,151,124,0) 70%);
  }
  .foliage--left { left: -20px; }
  .foliage--right { right: -20px; }
  .arrow { position: absolute; top: 188px; width: 22px; height: 24px; }
  .arrow--prev { left: 294px; }
  .arrow--next { left: 903px; }
  .label {
    position: absolute; left: 50%; top: 60px; transform: translateX(-50%);
    width: 340px; height: 300px;
    background: linear-gradient(160deg, var(--label-edge), var(--label) 60%);
    border-radius: 8px;
    display: flex; flex-direction: column; align-items: center; justify-content: center;
    color: var(--ink); text-align: center;
  }
  .shadow {
    position: absolute; left: 50%; top: 394px; transform: translateX(-50%);
    width: 320px; height: 14px; border-radius: 50%;
    background: radial-gradient(ellipse at center, rgba(60,60,60,.55), rgba(60,60,60,0) 70%);
  }
  .copy {
    position: absolute; left: 50%; top: 414px; transform: translateX(-50%);
    width: 650px; text-align: center;
    font-family: "Lato", sans-serif; font-size: 11.5px; line-height: 14.5px; color: var(--copy);
  }
  .brand {
    font-weight: 300; font-size: 20px; letter-spacing: .32em; color: var(--ink);
    margin-bottom: 12px; text-transform: uppercase;
  }
  .name { line-height: .95; margin-bottom: 12px; font-weight: 400; }
  .name--brush { font-family: "Caveat Brush", cursive; font-size: 40px; }
  .name--script { font-family: "Dancing Script", cursive; font-weight: 700; font-size: 40px; }
  .name--lime { color: var(--lime); }
  .name--gold { color: var(--gold); }
  .name--pink { color: var(--pink); }
  .name--crimson { color: var(--crimson); }
  .type { font-size: 13px; letter-spacing: .3em; text-transform: uppercase; line-height: 1.5; }
  .benefit { font-size: 9px; letter-spacing: .26em; text-transform: uppercase; color: var(--ink-soft); margin-top: 4px; line-height: 1.4; }
  .volume { font-size: 9px; letter-spacing: .2em; color: var(--ink-soft); margin-top: 6px; }
  .beard .brand { font-size: 15px; margin-bottom: 8px; }
  .rule { width: 140px; height: 1px; background: var(--white); margin: 6px 0; }
  .beard .tag { font-family: "Oswald", sans-serif; font-weight: 300; font-size: 12px; text-transform: uppercase; color: var(--white); }
  .beard .name--script { color: var(--white); font-size: 36px; margin: 2px 0 4px; }
  .beard .scent { font-family: "Oswald", sans-serif; font-weight: 300; font-size: 16px; text-transform: uppercase; color: var(--white); margin-top: 8px; }
</style>
</head>
<body>
<main class="range">

  <section class="product">
    <div class="foliage foliage--left" role="img" aria-label="Palm frond decoration"></div>
    <div class="foliage foliage--right" role="img" aria-label="Palm frond decoration"></div>
    <svg class="arrow arrow--prev" viewBox="0 0 22 24" aria-hidden="true"><polygon points="22,0 22,24 0,12" fill="var(--arrow)"/></svg>
    <svg class="arrow arrow--next" viewBox="0 0 22 24" aria-hidden="true"><polygon points="0,0 0,24 22,12" fill="var(--arrow)"/></svg>
    <div class="label">
      <p class="brand">Fern And Flint</p>
      <h2 class="name name--brush name--lime">Velvet<br>Grove</h2>
      <p class="type">Green<br>Clay Mask</p>
      <p class="benefit">Pore Tightening</p>
      <p class="volume">50ml</p>
    </div>
    <div class="shadow"></div>
    <p class="copy">Lorem ipsum dolor sit amet, consectetuer adipiscing elit, sed diam nonummy nibh euismod tincidunt ut laoreet dolore magna aliquam erat volutpat. Ut wisi enim ad minim veniam, quis nostrud exerci tation ullamcorper suscipit lobortis nisl ut aliquip ex ea commodo consequat.</p>
  </section>

  <section class="product">
    <div class="foliage foliage--left" role="img" aria-label="Palm frond decoration"></div>
    <div class="foliage foliage--right" role="img" aria-label="Palm frond decoration"></div>
    <svg class="arrow arrow--prev" viewBox="0 0 22 24" aria-hidden="true"><polygon points="22,0 22,24 0,12" fill="var(--arrow)"/></svg>
    <svg class="arrow arrow--next" viewBox="0 0 22 24" aria-hidden="true"><polygon points="0,0 0,24 22,12" fill="var(--arrow)"/></svg>
    <div class="label">
      <p class="brand">Fern And Flint</p>
      <h2 class="name name--brush name--gold">Golden<br>Glow</h2>
      <p class="type">Turmeric<br>Clay Cream Mask</p>
      <p class="benefit">Anti-Inflammatory<br>and Detoxifying</p>
      <p class="volume">50ml</p>
    </div>
    <div class="shadow"></div>
    <p class="copy">Lorem ipsum dolor sit amet, consectetuer adipiscing elit, sed diam nonummy nibh euismod tincidunt ut laoreet dolore magna aliquam erat volutpat. Ut wisi enim ad minim veniam, quis nostrud exerci tation ullamcorper suscipit lobortis nisl ut aliquip ex ea commodo consequat.</p>
  </section>

  <section class="product">
    <div class="foliage foliage--left" role="img" aria-label="Palm frond decoration"></div>
    <div class="foliage foliage--right" role="img" aria-label="Palm frond decoration"></div>
    <svg class="arrow arrow--prev" viewBox="0 0 22 24" aria-hidden="true"><polygon points="22,0 22,24 0,12" fill="var(--arrow)"/></svg>
    <svg class="arrow arrow--next" viewBox="0 0 22 24" aria-hidden="true"><polygon points="0,0 0,24 22,12" fill="var(--arrow)"/></svg>
    <div class="label">
      <p class="brand">Fern And Flint</p>
      <h2 class="name name--script name--pink">Rosy<br>Dreams</h2>
      <p class="type">Pink<br>Clay Cream Mask</p>
      <p class="benefit">Anti-Aging &amp; Pore Tightening</p>
      <p class="volume">50ml</p>
    </div>
    <div class="shadow"></div>
    <p class="copy">Lorem ipsum dolor sit amet, consectetuer adipiscing elit, sed diam nonummy nibh euismod tincidunt ut laoreet dolore magna aliquam erat volutpat. Ut wisi enim ad minim veniam, quis nostrud exerci tation ullamcorper suscipit lobortis nisl ut aliquip ex ea commodo consequat.</p>
  </section>

  <section class="product">
    <div class="foliage foliage--left" role="img" aria-label="Palm frond decoration"></div>
    <div class="foliage foliage--right" role="img" aria-label="Palm frond decoration"></div>
    <svg class="arrow arrow--prev" viewBox="0 0 22 24" aria-hidden="true"><polygon points="22,0 22,24 0,12" fill="var(--arrow)"/></svg>
    <svg class="arrow arrow--next" viewBox="0 0 22 24" aria-hidden="true"><polygon points="0,0 0,24 22,12" fill="var(--arrow)"/></svg>
    <div class="label">
      <p class="brand">Fern And Flint</p>
      <h2 class="name name--brush name--crimson">Crimson<br>Ember</h2>
      <p class="type">Green<br>Clay Mask</p>
      <p class="benefit">Hydrating and<br>Skin Regenerating</p>
      <p class="volume">50ml</p>
    </div>
    <div class="shadow"></div>
    <p class="copy">Lorem ipsum dolor sit amet, consectetuer adipiscing elit, sed diam nonummy nibh euismod tincidunt ut laoreet dolore magna aliquam erat volutpat. Ut wisi enim ad minim veniam, quis nostrud exerci tation ullamcorper suscipit lobortis nisl ut aliquip ex ea commodo consequat.</p>
  </section>

  <section class="product">
    <div class="foliage foliage--left" role="img" aria-label="Palm frond decoration"></div>
    <div class="foliage foliage--right" role="img" aria-label="Palm frond decoration"></div>
    <svg class="arrow arrow--prev" viewBox="0 0 22 24" aria-hidden="true"><polygon points="22,0 22,24 0,12" fill="var(--arrow)"/></svg>
    <svg class="arrow arrow--next" viewBox="0 0 22 24" aria-hidden="true"><polygon points="0,0 0,24 22,12" fill="var(--arrow)"/></svg>
    <div class="label beard">
      <p class="brand">Fern And Flint</p>
      <div class="rule"></div>
      <p class="tag">Premium Organic</p>
      <h2 class="name name--script">Beard Oil</h2>
      <div class="rule"></div>
      <p class="scent">Patchouli</p>
      <p class="volume">30ml</p>
    </div>
    <div class="shadow"></div>
    <p class="copy">Lorem ipsum dolor sit amet, consectetuer adipiscing elit, sed diam nonummy nibh euismod tincidunt ut laoreet dolore magna aliquam erat volutpat. Ut wisi enim ad minim veniam, quis nostrud exerci tation ullamcorper suscipit lobortis nisl ut aliquip ex ea commodo consequat.</p>
  </section>

</main>
</body>
</html>
```